Boutique Wealth management firm needs a new business card design

I want to update my business card design to be more consistent with the look and feel of my website (www.corvalen-capital.example). I would like to incorporate an ivory parchment background and am open to switching from the current "portrait" layout to a more traditional "landscape" orientation. The final design should convey stability and exclusivity and I want something in PDF format that is ready to send to the printer
Updates

Thank you all for taking the time to submit your designs for my project. I've made my decision and picked the design I like best. Thanks again!

Industry/Entity Type

Business

```html
<!DOCTYPE html>
<html lang="en">
<head>
<meta charset="utf-8">
<title>Corvalen Capital – Business Card</title>
<link rel="stylesheet" href="https://fonts.googleapis.com/css2?family=Arimo:wght@400;700&family=Tinos:wght@400&display=swap">
<style>
  :root {
    --page: #ffffff;
    --olive: #62560f;
    --maroon: #7a1a3f;
    --ink: #111111;
    --tan-text: #e9dcae;
    --parchment-light: #ecdcaa;
    --parchment-mid: #dcc38a;
    --parchment-dark: #c9a866;
  }
  html, body {
    margin: 0;
    width: 1200px;
    height: 1200px;
    overflow: hidden;
    background: var(--page);
  }
  .card {
    position: absolute;
    left: 222px;
    top: 371px;
    width: 754px;
    height: 456px;
    background: var(--olive);
    font-family: "Arimo", Arial, sans-serif;
    overflow: hidden;
  }
  .parchment {
    position: absolute;
    left: 0; top: 16px;
    width: 754px; height: 294px;
    background:
      radial-gradient(ellipse at 30% 40%, var(--parchment-light) 0%, transparent 60%),
      radial-gradient(ellipse at 80% 70%, var(--parchment-dark) 0%, transparent 55%),
      linear-gradient(135deg, var(--parchment-mid), var(--parchment-light) 45%, var(--parchment-mid));
  }
  .abs { position: absolute; line-height: 1; margin: 0; white-space: nowrap; }
  .brand {
    left: 42px; top: 66px;
    font-size: 31px; font-weight: 700;
    color: var(--maroon);
    letter-spacing: 1px;
  }
  .license { left: 463px; top: 58px; font-size: 15.5px; color: var(--ink); }
  .person-name { left: 43px; top: 178px; font-size: 24px; font-weight: 700; color: var(--maroon); }
  .person-title { left: 43px; top: 208px; font-size: 17px; color: var(--ink); }
  .tagline {
    right: 34px;
    font-family: "Tinos", "Times New Roman", serif;
    color: var(--maroon);
    text-align: right;
  }
  .tagline-top { top: 232px; font-size: 22px; }
  .tagline-main { top: 262px; font-size: 39px; }
  .tagline-main .small { font-size: 22px; }
  .rule { position: absolute; height: 2px; background: var(--maroon); top: 292px; }
  .rule-left { left: 0; width: 448px; }
  .rule-right { left: 730px; width: 24px; }
  .divider {
    position: absolute; left: 378px; top: 325px; width: 1px; height: 126px;
    background: linear-gradient(to bottom, rgba(233,220,174,0.1), rgba(233,220,174,0.7), rgba(233,220,174,0.1));
  }
  .contact { color: var(--tan-text); font-size: 20px; }
  .contact svg { position: absolute; left: -24px; top: 3px; width: 15px; height: 15px; }
  .c1 { left: 62px; top: 348px; }
  .c2 { left: 62px; top: 374px; }
  .c3 { left: 62px; top: 401px; }
  .a1 { left: 443px; top: 365px; }
  .a2 { left: 443px; top: 391px; }
</style>
</head>
<body>
  <div class="card">
    <div class="parchment" role="img" aria-label="Aged ivory parchment texture"></div>

    <p class="abs brand">CORVALEN CAPITAL</p>
    <p class="abs license">CA Insurance License #0K71842</p>

    <p class="abs person-name">Dana Whitlock, CFP</p>
    <p class="abs person-title">Principal</p>

    <p class="abs tagline tagline-top">Anchoring your</p>
    <p class="abs tagline tagline-main">Plans <span class="small">and</span> Legacy</p>
    <div class="rule rule-left"></div>
    <div class="rule rule-right"></div>

    <p class="abs contact c1">
      <svg viewBox="0 0 16 16" fill="none" stroke="currentColor" stroke-width="1.3"><circle cx="8" cy="8" r="7"/><path d="M5.5 4.5l1.3 1.6-.8 1c.6 1.2 1.4 2 2.6 2.6l1-.8 1.6 1.3-.8 1.2c-2.8-.4-5.2-2.8-5.6-5.6z" fill="currentColor" stroke="none"/></svg>
      555-014-2287
    </p>
    <p class="abs contact c2">
      <svg viewBox="0 0 16 16" fill="none" stroke="currentColor" stroke-width="1.3"><circle cx="8" cy="8" r="7"/><rect x="4.5" y="5.5" width="7" height="5"/><path d="M4.5 5.5l3.5 3 3.5-3"/></svg>
      dana@corvalen-capital.example
    </p>
    <p class="abs contact c3">
      <svg viewBox="0 0 16 16" fill="none" stroke="currentColor" stroke-width="1.2"><circle cx="8" cy="8" r="7"/><ellipse cx="8" cy="8" rx="3" ry="7"/><path d="M1 8h14M2.5 4.5h11M2.5 11.5h11"/></svg>
      www.corvalen-capital.example
    </p>

    <div class="divider"></div>

    <p class="abs contact a1">
      <svg viewBox="0 0 16 16" fill="currentColor"><path d="M8 1a4.5 4.5 0 0 0-4.5 4.5C3.5 9 8 15 8 15s4.5-6 4.5-9.5A4.5 4.5 0 0 0 8 1zm0 6.3a1.8 1.8 0 1 1 0-3.6 1.8 1.8 0 0 1 0 3.6z"/></svg>
      880 Harlow Ridge Rd. #214
    </p>
    <p class="abs contact a2">Fairmont, CA 94000</p>
  </div>
</body>
</html>
```